Business Card for Dental Office

Our office is in the Hillcrest section of San Diego, California which is a well-established area. Maybe the back can be a map of our office location

```html
<!DOCTYPE html>
<html lang="en">
<head>
<meta charset="utf-8">
<title>Crestview Dental – Business Card</title>
<link rel="stylesheet" href="https://fonts.googleapis.com/css2?family=Open+Sans:ital,wght@0,400;0,600;1,400&display=swap">
<style>
  :root {
    --page-bg: #e9e7e3;
    --card-white: #ffffff;
    --card-light: #f2f2f2;
    --band-grey: #9a9a9a;
    --text-grey: #808080;
    --text-dark: #6e6e6e;
    --swoosh-black: #111111;
    --rule-grey: #8c8c8c;
  }
  * { box-sizing: border-box; margin: 0; padding: 0; }
  html, body {
    width: 1200px; height: 900px; overflow: hidden;
    background: var(--page-bg);
    font-family: "Open Sans", sans-serif;
  }
  .sheet {
    position: relative; width: 1200px; height: 900px;
    display: flex; flex-direction: column; align-items: center; justify-content: center; gap: 48px;
  }
  .card {
    position: relative; width: 640px; height: 366px; overflow: hidden;
    box-shadow: 0 6px 18px rgba(0,0,0,0.18);
  }

  /* Appointment side */
  .appointment { background: var(--card-light); }
  .appointment__title {
    position: absolute; top: 68px; left: 0; width: 100%;
    text-align: center; font-size: 24px; font-weight: 400; letter-spacing: 1px; color: var(--text-grey);
  }
  .appointment__field {
    position: absolute; display: flex; align-items: flex-end;
    font-size: 21px; color: var(--text-grey);
  }
  .appointment__line {
    display: inline-block; border-bottom: 1.5px solid var(--rule-grey); height: 1px; margin-bottom: 6px;
  }
  .appointment__rule { position: absolute; top: 118px; left: 200px; width: 330px; border-bottom: 1.5px solid var(--rule-grey); }
  .field-name { top: 150px; left: 116px; }
  .field-name .appointment__line { width: 420px; }
  .field-date { top: 208px; left: 130px; }
  .field-date .line-date { width: 160px; }
  .field-date .line-time { width: 180px; }
  .appointment__band {
    position: absolute; left: 0; bottom: 0; width: 100%; height: 124px;
    background: var(--band-grey);
  }
  .appointment__notice {
    position: absolute; left: 0; bottom: 28px; width: 100%;
    text-align: center; font-style: italic; font-size: 16px; color: var(--card-white);
  }

  /* Contact side */
  .contact { background: var(--card-white); }
  .contact__swoosh { position: absolute; inset: 0; }
  .contact__name {
    position: absolute; top: 58px; left: 50px;
    font-weight: 600; font-size: 23px; color: var(--text-dark); letter-spacing: 0.3px;
  }
  .contact__role { position: absolute; top: 90px; left: 56px; font-size: 17px; color: var(--text-grey); }
  .contact__address {
    position: absolute; top: 152px; left: 60px;
    font-size: 18px; line-height: 25px; color: var(--text-grey);
  }
  .contact__lines { position: absolute; top: 214px; left: 66px; list-style: none; }
  .contact__lines li {
    display: flex; align-items: center; gap: 8px;
    font-size: 18px; line-height: 26px; color: var(--text-grey);
  }
  .contact__lines svg { width: 14px; height: 14px; fill: var(--text-dark); }
  .brand {
    position: absolute; top: 58px; right: 44px;
    display: flex; align-items: center; gap: 10px;
  }
  .brand__dot { width: 16px; height: 16px; border-radius: 50%; background: var(--text-grey); }
  .brand__name { font-size: 24px; color: var(--text-grey); }
  .contact__web {
    position: absolute; top: 222px; right: 30px;
    font-size: 15px; color: var(--card-white);
  }
</style>
</head>
<body>
<main class="sheet">

  <section class="card appointment" aria-label="Appointment card">
    <h2 class="appointment__title">APPOINTMENT</h2>
    <div class="appointment__rule"></div>
    <div class="appointment__field field-name">NAME<span class="appointment__line"></span></div>
    <div class="appointment__field field-date">DATE<span class="appointment__line line-date"></span>TIME<span class="appointment__line line-time"></span></div>
    <div class="appointment__band"></div>
    <p class="appointment__notice">If unable to keep the appointment please give 24 hours notice</p>
  </section>

  <section class="card contact" aria-label="Contact card">
    <svg class="contact__swoosh" viewBox="0 0 640 366" width="640" height="366" aria-hidden="true">
      <path d="M0,296 C240,300 430,200 640,120 V366 H0 Z" fill="var(--band-grey)"/>
      <path d="M0,296 C150,298 330,262 530,164 C400,250 220,335 0,338 Z" fill="var(--swoosh-black)"/>
      <path d="M530,164 C400,250 220,335 0,338" fill="none" stroke="var(--card-white)" stroke-width="3"/>
    </svg>

    <h1 class="contact__name">DANIEL REYES</h1>
    <p class="contact__role">Managing Director</p>

    <p class="contact__address">1234, Address GoesHere,<br>Country name, 12345</p>
    <ul class="contact__lines">
      <li><svg viewBox="0 0 24 24"><path d="M6.6 10.8a15.2 15.2 0 0 0 6.6 6.6l2.2-2.2a1 1 0 0 1 1-.25 11.4 11.4 0 0 0 3.6.57 1 1 0 0 1 1 1V20a1 1 0 0 1-1 1A17 17 0 0 1 3 4a1 1 0 0 1 1-1h3.5a1 1 0 0 1 1 1c0 1.25.2 2.45.57 3.57a1 1 0 0 1-.25 1z"/></svg>(044)123456789</li>
      <li><svg viewBox="0 0 24 24"><path d="M2 5h20v14H2z" fill="var(--text-dark)"/><path d="M3 6l9 7 9-7" fill="none" stroke="#fff" stroke-width="1.5"/></svg>info@youremail.com</li>
    </ul>

    <div class="brand">
      <span class="brand__dot"></span>
      <span class="brand__name">Crestview Dental</span>
    </div>

    <p class="contact__web">www.websitename.com</p>
  </section>

</main>
</body>
</html>
```